Retiros Silencio

I want a Catholic flyer, with the Virgen Mary showing aiding, praying, and Jesus carrying the cross, to invite people to a silent retreat. The retreats are monthly. For women, they are Feb. 21, March 21, etc (every third Saturday), and for men they are Feb. 28, March 28, etc (every fourth Saturday). I want each month date to show for both women and men. Our logo should be in there, which is similar to the Holy family icon attached. Also, show that cost is $80, and the place for the retreats is Casa Alborada, 4187 Juniper Ct, Falls Church, VA and for more information to contact, for women 540-555-0147 and for men 571-555-0182. I will use the flyer for around 4 x 6 or 3 x 5 postcard. Organizers are: Nidos de Valle Claro. The flyer needs to be in spanish "RETIROS EN SILENCIO" and the months should be labeled in Spanish too.

```html
<!DOCTYPE html>
<html lang="es">
<head>
<meta charset="utf-8">
<title>Retiros en Silencio – Nidos de Valle Claro</title>
<link rel="stylesheet" href="https://fonts.googleapis.com/css2?family=Montserrat:wght@800;900&family=Figtree:wght@500;600&display=swap">
<style>
  :root {
    --backdrop: #2b2b2d;
    --paper: #ffffff;
    --red: #d2152f;
    --red-deep: #a3121f;
    --panel-light: #cc1c36;
    --panel-dark: #7e0a1d;
    --gold: #f3b733;
    --gold-dark: #c9962a;
    --ink: #111111;
    --white: #ffffff;
  }
  * { margin: 0; padding: 0; box-sizing: border-box; }
  html, body { width: 1200px; height: 804px; overflow: hidden; background: var(--backdrop); }
  body { position: relative; font-family: "Figtree", "Helvetica Neue", Arial, sans-serif; }

  .postcard { position: absolute; left: 52px; top: 37px; width: 1096px; height: 731px; }

  .info-side { position: absolute; left: 0; top: 0; width: 371px; height: 731px; background: var(--paper); }
  .ribbon { position: absolute; left: 19px; top: 0; width: 314px; height: 299px; }
  .emblem-cross { position: absolute; left: 162px; top: 14px; width: 48px; height: 52px; }
  .emblem-icon { position: absolute; left: 71px; top: 64px; width: 229px; height: 325px; }

  .label { position: absolute; left: 72px; font-family: "Montserrat", sans-serif; font-weight: 900; color: var(--red); font-size: 28px; letter-spacing: 0.5px; line-height: 1; }
  .detail { position: absolute; left: 72px; font-size: 21px; font-weight: 500; color: var(--ink); line-height: 24.5px; }
  .label--place { top: 410px; }
  .detail--place { top: 436px; }
  .label--contact { top: 535px; }
  .detail--contact { top: 561px; }

  .cost-tag { position: absolute; left: 71px; top: 640px; width: 233px; height: 51px; background: var(--red); color: var(--white); font-family: "Figtree", sans-serif; font-weight: 600; font-size: 32px; display: flex; align-items: center; justify-content: center; }

  .invite-side { position: absolute; left: 371px; top: 0; width: 725px; height: 731px;
    background: radial-gradient(ellipse at 78% 60%, #a8162b 0%, transparent 55%),
                linear-gradient(100deg, var(--panel-light) 0%, #bd1830 45%, var(--panel-dark) 100%); }

  .invite-copy { position: absolute; left: 43px; top: 0; width: 680px; color: var(--white); }
  .title { position: absolute; top: 19px; left: 0; font-family: "Montserrat", sans-serif; font-weight: 900; font-size: 96px; line-height: 97px; letter-spacing: 2.5px; white-space: nowrap; }
  .organizer { position: absolute; top: 213px; left: 0; color: var(--gold); font-weight: 600; font-size: 44px; line-height: 1; white-space: nowrap; }
  .intro, .closing { position: absolute; left: 0; font-size: 21.5px; font-weight: 500; line-height: 24.5px; white-space: nowrap; }
  .intro { top: 274px; }
  .schedule { position: absolute; left: 0; white-space: nowrap; }
  .schedule--women { top: 410px; }
  .schedule--men { top: 501px; }
  .schedule-heading { color: var(--gold); font-size: 21.5px; font-weight: 500; line-height: 24.5px; }
  .schedule-dates { font-size: 22px; font-weight: 500; line-height: 24.5px; }
  .closing { top: 594px; }
  .footer { position: absolute; top: 662px; left: 0; font-size: 21.5px; font-weight: 500; display: flex; align-items: center; white-space: nowrap; }
  .footer-web { color: var(--gold); display: flex; align-items: center; margin-left: 16px; }
  .footer-web svg { margin-right: 8px; }
</style>
</head>
<body>
<main class="postcard">
  <section class="info-side">
    <svg class="ribbon" viewBox="0 0 314 299" aria-hidden="true">
      <defs>
        <linearGradient id="ribbonFill" x1="0" x2="1">
          <stop offset="0" stop-color="#d81a35"/>
          <stop offset="1" stop-color="#a51226"/>
        </linearGradient>
      </defs>
      <polygon points="0,0 314,0 314,299 157,269 0,299" fill="url(#ribbonFill)"/>
    </svg>
    <svg class="emblem-cross" viewBox="0 0 48 52" aria-hidden="true">
      <rect x="20" y="0" width="8" height="52" fill="var(--gold-dark)"/>
      <rect x="0" y="19" width="48" height="8" fill="var(--gold-dark)"/>
    </svg>
    <svg class="emblem-icon" viewBox="0 0 229 325" role="img" aria-label="Icono de la Sagrada Familia en marco dorado">
      <defs>
        <linearGradient id="iconFill" x1="0" y1="0" x2="0" y2="1">
          <stop offset="0" stop-color="#c8a24a"/>
          <stop offset="0.5" stop-color="#a8262a"/>
          <stop offset="1" stop-color="#c3662c"/>
        </linearGradient>
      </defs>
      <polygon points="114.5,0 229,50 229,325 0,325 0,50" fill="#6e5a3a"/>
      <polygon points="114.5,22 200,60 200,295 29,295 29,60" fill="url(#iconFill)"/>
    </svg>

    <h2 class="label label--place">LUGAR:</h2>
    <p class="detail detail--place">Casa Alborada<br>4187 Juniper Ct<br>Falls Church, VA</p>
    <h2 class="label label--contact">INFORMACIÓN:</h2>
    <p class="detail detail--contact">Mujeres: 540-555-0147<br>Hombres: 571-555-0182</p>
    <div class="cost-tag">COSTO: $80</div>
  </section>

  <section class="invite-side" role="img" aria-label="Pintura de Jesús cargando la cruz en tonos rojos">
    <div class="invite-copy">
      <h1 class="title">RETIROS EN<br>SILENCIO</h1>
      <p class="organizer">Nidos de Valle Claro</p>
      <p class="intro">Ven y encuentra la paz en el silencio con la Virgen María y Jesús.<br>Un día de retiro para renovar tu corazón y fortalecer tu fe.</p>

      <div class="schedule schedule--women">
        <p class="schedule-heading">Para Mujeres – Cada tercer sábado del mes</p>
        <p class="schedule-dates">17 Ene • 21 Feb • 21 Mar • 18 Abr • 16 May • 20 Jun • 18 Jul<br>15 Ago • 19 Sep • 17 Oct • 21 Nov • 19 Dic</p>
      </div>
      <div class="schedule schedule--men">
        <p class="schedule-heading">Para Hombres – Cada cuarto sábado del mes</p>
        <p class="schedule-dates">24 Ene • 28 Feb • 28 Mar • 25 Abr • 23 May • 27 Jun • 25 Jul<br>22 Ago • 26 Sep • 24 Oct • 28 Nov • 26 Dic</p>
      </div>

      <p class="closing">Con la Virgen María intercediendo y Jesús cargando la cruz,<br>vivamos juntos un encuentro de fe, oración y silencio.</p>

      <p class="footer">Nidos de Valle Claro
        <span class="footer-web">
          <svg width="18" height="13" viewBox="0 0 18 13" aria-hidden="true">
            <rect width="18" height="13" fill="var(--gold)"/>
            <polyline points="1,1 9,7 17,1" fill="none" stroke="#b3152b" stroke-width="1.6"/>
          </svg>valleclaroretiros.org
        </span>
      </p>
    </div>
  </section>
</main>
</body>
</html>
```